Classy business card for accounting firm

We're looking for a new business card for our accounting firm. Our logo was designed by Brandolith, so all of the design info we would like to use has been provided. The specific font provided isn't required to be used.

We want the card to look classy and elegent. Probably more minimalistic, but still with some pops of color.

The options we would like to include on the card are as follows:
1. Main office phone line
2. Direct phone line
3. Email address
4. Website URL
5. Name
6. Title (CEO, President, etc.)
7. Firm Address

The design and card should be double sided!!! The drop down box in the project brief for some reason is defaulting to single sided. Not sure why this is happening.

Thanks!

Contact Information for Business Card

The options we would like to include on the card are as follows: 1. Main office phone line 2. Direct phone line 3. Email address 4. Website URL 5. Name 6. Title (CEO, President, etc.) 7. Firm Address

Requirements
Must have
• Card must be double sided.

```html
<!DOCTYPE html>
<html lang="en">
<head>
<meta charset="utf-8">
<title>Ledgerline Associates – Business Card</title>
<link rel="stylesheet" href="https://fonts.googleapis.com/css2?family=Mulish:wght@400;600;700;800&family=Arimo:wght@400;700&display=swap">
<style>
  :root {
    --stage: #1b1b1c;
    --card: #323233;
    --card-deep: #2b2b2c;
    --edge: #f27a12;
    --accent: #f58220;
    --leaf: #9cc23a;
    --ink: #ffffff;
    --ink-soft: #d9d9d9;
    --rule: #bdbdbd;
  }
  * { margin: 0; padding: 0; box-sizing: border-box; }
  html, body { width: 1200px; height: 900px; overflow: hidden; background: var(--stage); }
  .stage { position: relative; width: 1200px; height: 900px; }

  .card {
    position: absolute;
    width: 630px;
    height: 360px;
    border-radius: 26px;
    background: var(--card);
    border: 3px solid var(--edge);
    overflow: hidden;
    color: var(--ink);
  }
  .card--back { left: 500px; top: 70px; background: linear-gradient(160deg, #38383a 0%, var(--card) 45%, var(--card-deep) 100%); }
  .card--front { left: 70px; top: 470px; }

  /* Company lockup */
  .lockup { position: absolute; text-align: right; }
  .lockup__name {
    font-family: "Mulish", sans-serif;
    font-weight: 700;
    font-size: 30px;
    letter-spacing: 3px;
    white-space: nowrap;
  }
  .lockup__tag {
    display: flex; align-items: center; justify-content: flex-end; gap: 10px;
    font-family: "Mulish", sans-serif;
    font-weight: 600;
    font-size: 12.5px;
    letter-spacing: 2.6px;
    margin-top: 4px;
    white-space: nowrap;
  }
  .lockup__tag::before, .lockup__tag::after {
    content: ""; width: 40px; height: 2px; background: var(--leaf);
  }
  .card--back .lockup { right: 34px; bottom: 52px; }

  .card--front .lockup { right: 38px; top: 50px; }
  .card--front .lockup__name { font-size: 22px; letter-spacing: 2px; line-height: 28px; }
  .card--front .lockup__tag { font-size: 10.5px; letter-spacing: 2.2px; margin-top: 2px; }
  .card--front .lockup__tag::before, .card--front .lockup__tag::after { width: 30px; }
  .lockup__square {
    display: block; width: 30px; height: 30px; background: var(--accent);
    margin: 0 110px 10px auto;
  }

  /* Front details */
  .person { position: absolute; left: 38px; top: 92px; }
  .person__name {
    font-family: "Mulish", sans-serif; font-weight: 800; font-size: 20px;
    color: var(--accent); letter-spacing: 0.5px; line-height: 26px; white-space: nowrap;
  }
  .person__title { font-family: "Arimo", sans-serif; font-size: 14px; color: var(--ink-soft); margin-top: 2px; white-space: nowrap; }

  .divider { position: absolute; left: 38px; right: 38px; top: 158px; height: 1.5px; background: var(--rule); }

  .contacts { position: absolute; left: 38px; top: 180px; list-style: none; }
  .contacts li {
    display: flex; align-items: center; gap: 9px;
    font-family: "Arimo", sans-serif; font-size: 15px; color: var(--ink-soft);
    line-height: 25px; white-space: nowrap;
  }
  .contacts svg { width: 13px; height: 13px; flex: none; }

  .address {
    position: absolute; right: 46px; bottom: 50px;
    font-family: "Arimo", sans-serif; font-style: normal; font-size: 19px; line-height: 26px;
    color: var(--ink-soft); white-space: nowrap;
  }
</style>
</head>
<body>
<main class="stage">

  <section class="card card--back" aria-label="Card back">
    <div class="lockup">
      <div class="lockup__name">LEDGERLINE ASSOCIATES</div>
      <div class="lockup__tag">SOLVING TAX PROBLEMS</div>
    </div>
  </section>

  <section class="card card--front" aria-label="Card front">
    <div class="person">
      <div class="person__name">MARCUS HALE</div>
      <div class="person__title">CEO, President</div>
    </div>

    <div class="lockup">
      <span class="lockup__square"></span>
      <div class="lockup__name">LEDGERLINE ASSOCIATES</div>
      <div class="lockup__tag">SOLVING TAX PROBLEMS</div>
    </div>

    <div class="divider"></div>

    <ul class="contacts">
      <li>
        <svg viewBox="0 0 16 16" aria-hidden="true"><path fill="#f58220" d="M3.5 1.5l2.6 2.6-1.4 1.9c.9 2 2.5 3.6 4.5 4.5l1.9-1.4 2.6 2.6-1.6 2.1C7 13.4 2.6 9 1.4 3.1z"/></svg>
        123-456-2100
      </li>
      <li>
        <svg viewBox="0 0 16 16" aria-hidden="true"><rect x="4" y="1" width="8" height="14" rx="1.5" fill="none" stroke="#f58220" stroke-width="1.6"/><circle cx="8" cy="12.3" r="0.9" fill="#f58220"/></svg>
        123-456-2100
      </li>
      <li>
        <svg viewBox="0 0 16 16" aria-hidden="true"><rect x="1.5" y="3" width="13" height="10" rx="1" fill="none" stroke="#f58220" stroke-width="1.6"/><path d="M2 4l6 5 6-5" fill="none" stroke="#f58220" stroke-width="1.6"/></svg>
        hello@ledgerlinetax.com
      </li>
      <li>
        <svg viewBox="0 0 16 16" aria-hidden="true"><circle cx="8" cy="8" r="6.5" fill="none" stroke="#f58220" stroke-width="1.5"/><path d="M1.5 8h13M8 1.5c-3 3.5-3 9.5 0 13M8 1.5c3 3.5 3 9.5 0 13" fill="none" stroke="#f58220" stroke-width="1.2"/></svg>
        www.ledgerlinetax.com
      </li>
    </ul>

    <address class="address">
      Your Address, City<br>
      State, Zip 0000
    </address>
  </section>

</main>
</body>
</html>
```